Business Card Design

I am nail technician working from home in Mount Helena, Perth and I require new business cards. I only work with Gel medium for nail extensions using tips or I can also do sculpture nails. I specialise in hand painted nail art using water based acrylic paint and nail polish. As the name suggest I love all things "Velvet" so I would love something that reflects this while also being professional. I'm also on Trendlo and would the Trendlo logo.

Contact Information for Business Card

Velvet Comet nail designs,Rosalind ,0417859273, VelvetCometnaildesigns@quorvia.com, nail technician specialising in hand painted nail art, only using a Gel medium

```html
<!DOCTYPE html>
<html lang="en">
<head>
<meta charset="utf-8">
<title>Velvet Comet Nail Designs – Business Card</title>
<link href="https://fonts.googleapis.com/css2?family=Lato:wght@400;700&family=Fira+Sans:wght@400&display=swap" rel="stylesheet">
<style>
  :root {
    --brand-red: #d8262b;
    --card-white: #ffffff;
    --text-grey: #6b6b6b;
    --stage: #e9e6e1;
    --shadow: rgba(0,0,0,0.18);
  }
  * { margin: 0; padding: 0; box-sizing: border-box; }
  html, body { width: 1200px; height: 1000px; overflow: hidden; }
  body {
    background: var(--stage);
    font-family: "Lato", sans-serif;
    position: relative;
  }
  .card {
    position: absolute;
    left: 320px;
    width: 560px;
    height: 320px;
    border-radius: 18px;
    box-shadow: 0 10px 24px var(--shadow);
    overflow: hidden;
  }
  .card--front { top: 130px; background: var(--card-white); }
  .card--back { top: 550px; background: var(--brand-red); }

  .edge-tab {
    position: absolute;
    left: 0;
    top: 178px;
    width: 26px;
    height: 36px;
  }
  .wordmark { color: var(--brand-red); font-weight: 400; line-height: 1; }
  .card--front .wordmark { position: absolute; left: 52px; top: 74px; }
  .wordmark__main { display: block; font-size: 50px; }
  .wordmark__sub { display: block; font-size: 24px; margin-top: 4px; padding-left: 150px; }

  .holder { position: absolute; left: 104px; top: 186px; }
  .holder__name { color: var(--brand-red); font-weight: 700; font-size: 17px; letter-spacing: 1.5px; }
  .holder__role { color: var(--text-grey); font-size: 12px; margin-top: 1px; }

  .contact { position: absolute; left: 104px; top: 240px; list-style: none; font-size: 13px; color: var(--text-grey); line-height: 19px; }
  .contact b { color: var(--brand-red); font-weight: 700; }

  .social { position: absolute; right: 24px; top: 22px; display: flex; align-items: center; gap: 6px; font-size: 12px; color: var(--text-grey); }
  .social__dot { width: 8px; height: 8px; border-radius: 50%; background: var(--brand-red); }
  .social__network { color: var(--brand-red); }

  .card--back .wordmark { position: absolute; left: 150px; top: 58px; color: var(--card-white); }
  .card--back .wordmark__main { font-size: 62px; }
  .card--back .wordmark__sub { font-size: 28px; padding-left: 170px; }
  .tagline {
    position: absolute; left: 40px; top: 218px; width: 400px;
    font-family: "Fira Sans", sans-serif; font-size: 15px; line-height: 21px;
    color: var(--card-white); letter-spacing: 0.5px;
  }
  .back-tab { position: absolute; right: 0; top: 140px; width: 10px; height: 40px; background: var(--card-white); }
</style>
</head>
<body>
  <section class="card card--front" aria-label="Business card front">
    <svg class="edge-tab" viewBox="0 0 26 36" aria-hidden="true">
      <polygon points="0,0 26,0 22,4 26,8 22,12 26,16 22,20 26,24 22,28 26,32 22,36 0,36" fill="var(--brand-red)"/>
    </svg>
    <div class="wordmark">
      <span class="wordmark__main">Velvet Comet</span>
      <span class="wordmark__sub">Nail Designs</span>
    </div>
    <div class="holder">
      <p class="holder__name">ROSALIND</p>
      <p class="holder__role">Nail Technician</p>
    </div>
    <ul class="contact">
      <li><b>P:</b> 0417859273</li>
      <li><b>E:</b> VelvetCometnaildesigns@quorvia.com</li>
      <li><b>A:</b> Larkvale, Western Australia 6091</li>
    </ul>
    <div class="social">
      <span class="social__dot"></span>
      <span class="social__network">Trendlo</span>
      <span>@VelvetCometNailDesigns</span>
    </div>
  </section>

  <section class="card card--back" aria-label="Business card back">
    <div class="wordmark">
      <span class="wordmark__main">Velvet Comet</span>
      <span class="wordmark__sub">Nail Designs</span>
    </div>
    <p class="tagline">Nail Technician Specialising in Hand Painted Nail Art, Only Using a Gel Medium.</p>
    <div class="back-tab"></div>
  </section>
</body>
</html>
```